Velmo BUSINESS CARD

Design an attention-grabbing business cards. Draw inspiration from the provided logo file. Please use the same font style as in the logo.
the back side of the card is for accent/decoration.

Contact Information for Business Card

PLEASE USE PROVIDED BUSINESS CARD SAMPLE

Other font styles liked:
• LUMETTE

Colors
EB3D1F
EC4F4E
F09395
F8D3D4
FCEDEE

Requirements
Must have
• RED, BLACK COLORS, SOLID BACK COLOR
Nice to have
• MAKE IT FANCY

```html
<!DOCTYPE html>
<html lang="en">
<head>
<meta charset="utf-8">
<title>Velmo Business Card</title>
<link href="https://fonts.googleapis.com/css2?family=Poppins:wght@400;500;600&display=swap" rel="stylesheet">
<style>
  :root {
    --page-bg: #e3e3e3;
    --card-bg: #ffffff;
    --brand-red: #dc2430;
    --ink: #1d1d1d;
    --muted: #555555;
  }
  * { margin: 0; padding: 0; box-sizing: border-box; }
  html, body { width: 1200px; height: 900px; overflow: hidden; }
  body {
    background: var(--page-bg);
    font-family: "Poppins", sans-serif;
    color: var(--ink);
    position: relative;
  }
  .card {
    position: absolute;
    top: 217px;
    width: 308px;
    height: 499px;
    background: var(--card-bg);
    box-shadow: 2px 3px 3px rgba(0,0,0,0.35);
  }
  .card--back {
    left: 279px;
    border-radius: 0 60px 0 60px;
  }
  .card--front {
    left: 617px;
    border-radius: 60px 0 60px 0;
  }
  .back-emblem {
    position: absolute;
    left: 21px;
    top: 121px;
    width: 266px;
    height: 266px;
  }
  .brand {
    position: absolute;
    left: 35px;
    top: 123px;
    display: flex;
    align-items: center;
  }
  .brand__square {
    width: 47px;
    height: 47px;
    background: var(--ink);
    margin-right: 9px;
  }
  .brand__name {
    font-weight: 600;
    font-size: 44px;
    letter-spacing: 3px;
    line-height: 1;
    color: var(--ink);
  }
  .brand__tagline {
    position: absolute;
    left: 106px;
    top: 175px;
    font-size: 8px;
    letter-spacing: 1px;
    color: var(--muted);
    white-space: nowrap;
  }
  .person {
    position: absolute;
    left: 31px;
    top: 278px;
  }
  .person__name {
    font-weight: 600;
    font-size: 21px;
    letter-spacing: 0.5px;
    color: var(--brand-red);
    line-height: 1.1;
    word-spacing: 4px;
  }
  .person__role {
    font-size: 15px;
    line-height: 1.2;
  }
  .contacts {
    position: absolute;
    left: 32px;
    top: 332px;
    list-style: none;
  }
  .contacts li {
    display: flex;
    align-items: center;
    height: 18px;
    font-size: 15px;
    white-space: nowrap;
  }
  .contacts svg {
    width: 13px;
    height: 13px;
    margin-right: 9px;
    flex: none;
  }
  .address {
    position: absolute;
    left: 33px;
    top: 424px;
    font-size: 15px;
    line-height: 18px;
    font-style: normal;
    white-space: nowrap;
  }
</style>
</head>
<body>

<section class="card card--back">
  <svg class="back-emblem" viewBox="0 0 266 266" role="img" aria-label="Velmo brand emblem area">
    <circle cx="133" cy="133" r="133" fill="#dc2430"/>
  </svg>
</section>

<section class="card card--front">
  <div class="brand">
    <div class="brand__square"></div>
    <span class="brand__name">VELMO</span>
  </div>
  <p class="brand__tagline">A BOLD FORCE IN 3PL</p>

  <div class="person">
    <h1 class="person__name">DANA RIVERS</h1>
    <p class="person__role">President</p>
  </div>

  <ul class="contacts">
    <li>
      <svg viewBox="0 0 16 16" fill="none" stroke="#dc2430" stroke-width="1.8"><path d="M3 2l3 0 1 4-2 1c1 2 2 3 4 4l1-2 4 1 0 3c-7 1-12-4-11-11z"/></svg>
      317-555-0142
    </li>
    <li>
      <svg viewBox="0 0 16 16" fill="none" stroke="#dc2430" stroke-width="1.8"><rect x="4" y="1" width="8" height="14" rx="1.5"/><circle cx="8" cy="12.5" r="0.6" fill="#dc2430"/></svg>
      317-555-0187
    </li>
    <li>
      <svg viewBox="0 0 16 16"><rect x="1" y="3" width="14" height="10" fill="#dc2430"/><path d="M1 3l7 6 7-6" fill="none" stroke="#fff" stroke-width="1.4"/></svg>
      DRivers@velmo-llc.com
    </li>
    <li>
      <svg viewBox="0 0 16 16" fill="none" stroke="#dc2430" stroke-width="1.4"><circle cx="8" cy="8" r="6.5"/><ellipse cx="8" cy="8" rx="3" ry="6.5"/><path d="M1.5 8h13M2.5 5h11M2.5 11h11"/></svg>
      www.Velmo-LLC.com
    </li>
  </ul>

  <address class="address">
    1845&nbsp; N. 200 east<br>
    Brookdale. IN, 46210
  </address>
</section>

</body>
</html>
```